Vehicles Brochure Diagram

Task Outline
Create diagrams for our new vehicles brochures

Task Description

Who are we:
TLR is New Zealand's largest Business Group Buying organisation, helping organisations nationwide reduce their running costs. We offer members the best deals from over 100 Contracted Suppliers, anything from vehicles, stationery to electronics and coffee.

The project:
We need 2 diagrams to illustrate the benefits of our vehicle services. The diagram will be used in our brochures (example attached)

1. A Diagram illustrating/explaining the elements that are involved in purchasing a new car & how our service ties it all together to provide the best solution.
- Please see the Diagram 1 PDF for a rough wireframe of the elements involved

2. Another small diagram inserted on an separate page to demonstrate how our services can increase safety & profit and reduce costs & risks (PDF: Diagram 2 Details)

The design needs to be clean, clear and simple that it’s easy to understand within a few seconds of looking at it. Feel free to explore with different elements in the realm of infographics, flowcharts & diagrams to best communicate the idea visually.
Updates

Just thought I’ll share some of the feedback we’re giving tosubmissions that have been coming through to help with new submissions

-Challenge & be creative about the ways you demonstratethe elements

-We don’t want to see your design replicating the ones that isdrawn. The purpose of it is only to provide you with the content in context

-We can’t emphasis enough that the style pdf is only areference and not the look you should imitate. 

If you have any question please feel free to contact me.Looking forward to see your designs!

Reason: We're keen to see more approaches & creative ways of interpreting the content rather than a standard cycle diagram. Entries so far have been good but quite literal, we will provide feedback to help steer it in the right direction.

Target Market(s)

Business professionals, Decision makers on a corporate level & prospects.

Industry/Entity Type

Electronics

Requirements
Must have

• Likes – simple, clean & clear, uncluttered

Dislikes – Overcrowded images, text, & colours. Overly expressive typeface. Please no literal illustration of our sketches or colored version of our sketch.

Font: -Myriad Pro

Colour: Please refer to the color palette in the ‘Diagram Color & Style’ PDF

The brochures are attached with content to provide context that might inform the design better,

Dimensions & the amount of space you have to work with will also be highlighted

```html
<!DOCTYPE html>
<html lang="en">
<head>
<meta charset="utf-8">
<title>Vehicle Lifecycle Diagram</title>
<link href="https://fonts.googleapis.com/css2?family=Source+Sans+3:wght@400;700&display=swap" rel="stylesheet">
<style>
  :root {
    --page-bg: #ececec;
    --panel-bg: #ffffff;
    --panel-edge: #cfcfcf;
    --green-title: #2e5b2c;
    --body-grey: #7a7a7a;
    --green-light: #86ad5e;
    --green-dark: #2d5a2e;
    --green-rim: #6d9f45;
    --blue-light: #a9c5e6;
    --blue-dark: #2a4d8c;
    --blue-rim: #2f5597;
    --arrow-light: #9cc3e6;
    --arrow-dark: #2d4f91;
    --icon: #ffffff;
  }
  html, body { margin: 0; padding: 0; overflow: hidden; }
  body {
    width: 1200px; height: 900px; position: relative;
    background: var(--page-bg);
    font-family: "Source Sans 3", sans-serif;
  }
  .diagram-panel {
    position: absolute; left: 82px; top: 125px; width: 1034px; height: 647px;
    background: var(--panel-bg); border: 1px solid var(--panel-edge);
  }
  .diagram-art { position: absolute; left: 0; top: 0; }
  .stage-label { position: absolute; }
  .stage-title {
    margin: 0 0 6px; font-size: 19px; font-weight: 700; line-height: 22px;
    color: var(--green-title);
  }
  .stage-items {
    margin: 0; padding: 0; list-style: none; font-size: 15px; line-height: 21px;
    color: var(--body-grey);
  }
  .label-end-of-life { left: 383px; top: 231px; }
  .label-cost-to-run { left: 712px; top: 220px; }
  .label-company { left: 383px; top: 567px; }
  .label-cost-to-manage { left: 712px; top: 565px; }
  .hub-caption {
    position: absolute; left: 480px; width: 216px; top: 484px; text-align: center;
    color: #fff; font-size: 17px; font-weight: 700;
  }
</style>
</head>
<body>
<div class="diagram-panel"></div>

<svg class="diagram-art" width="1200" height="900" viewBox="0 0 1200 900">
  <defs>
    <linearGradient id="tile-green" x1="0" y1="0" x2="1" y2="1">
      <stop offset="0" stop-color="var(--green-light)"/>
      <stop offset="0.55" stop-color="#3f6e38"/>
      <stop offset="1" stop-color="var(--green-dark)"/>
    </linearGradient>
    <linearGradient id="tile-blue" x1="0" y1="0" x2="1" y2="1">
      <stop offset="0" stop-color="var(--blue-light)"/>
      <stop offset="0.5" stop-color="#4f77b5"/>
      <stop offset="1" stop-color="var(--blue-dark)"/>
    </linearGradient>
    <linearGradient id="arrow-top" x1="0" y1="0" x2="1" y2="0">
      <stop offset="0" stop-color="var(--arrow-dark)"/><stop offset="1" stop-color="var(--arrow-light)"/>
    </linearGradient>
    <linearGradient id="arrow-right" x1="0" y1="0" x2="0" y2="1">
      <stop offset="0" stop-color="var(--arrow-light)"/><stop offset="1" stop-color="var(--arrow-dark)"/>
    </linearGradient>
    <linearGradient id="arrow-bottom" x1="1" y1="0" x2="0" y2="0">
      <stop offset="0" stop-color="var(--arrow-dark)"/><stop offset="1" stop-color="var(--arrow-light)"/>
    </linearGradient>
    <linearGradient id="arrow-left" x1="0" y1="1" x2="0" y2="0">
      <stop offset="0" stop-color="var(--arrow-light)"/><stop offset="1" stop-color="var(--arrow-dark)"/>
    </linearGradient>
    <symbol id="car" viewBox="0 0 56 26">
      <path d="M2 20 L2 13 Q3 10 9 9 L16 9 L22 2 L38 2 L46 9 Q54 10 54 14 L54 20 Z" fill="var(--icon)"/>
      <circle cx="13" cy="20" r="4.5" fill="var(--icon)" stroke="#3d64a6" stroke-width="2"/>
      <circle cx="43" cy="20" r="4.5" fill="var(--icon)" stroke="#3d64a6" stroke-width="2"/>
    </symbol>
  </defs>

  <!-- cycle arrows -->
  <g class="cycle-arrows" fill="none" stroke-width="7">
    <path d="M395 203 Q590 150 780 190" stroke="url(#arrow-top)"/>
    <polygon points="775,176 813,200 771,210" fill="var(--arrow-light)" stroke="none"/>
    <path d="M993 345 Q1040 450 1006 535" stroke="url(#arrow-right)"/>
    <polygon points="992,530 1020,540 990,562" fill="var(--arrow-dark)" stroke="none"/>
    <path d="M808 688 Q600 760 408 696" stroke="url(#arrow-bottom)"/>
    <polygon points="410,680 375,688 402,712" fill="var(--arrow-light)" stroke="none"/>
    <path d="M196 543 Q150 440 195 368" stroke="url(#arrow-left)"/>
    <polygon points="181,370 205,335 211,374" fill="var(--arrow-dark)" stroke="none"/>
  </g>

  <!-- stage tiles -->
  <g class="stage-tiles" stroke="var(--green-rim)" stroke-width="4" fill="url(#tile-green)">
    <rect x="218" y="186" width="145" height="146" rx="30"/>
    <rect x="832" y="186" width="145" height="146" rx="30"/>
    <rect x="218" y="547" width="145" height="146" rx="30"/>
    <rect x="832" y="547" width="145" height="146" rx="30"/>
  </g>

  <!-- end of life icon: towed car -->
  <g class="icon-tow" fill="var(--icon)">
    <use href="#car" x="228" y="232" width="78" height="36" transform="rotate(-22 267 250)"/>
    <path d="M300 248 L322 232 L356 254 L356 262 L320 240 Z"/>
    <circle cx="322" cy="234" r="6"/>
    <path d="M315 240 Q312 252 304 252" fill="none" stroke="var(--icon)" stroke-width="3"/>
  </g>

  <!-- cost to run icon: oil bottle and wheel -->
  <g class="icon-run" fill="var(--icon)">
    <rect x="862" y="209" width="8" height="8"/>
    <path d="M852 222 L866 216 L880 222 L880 272 L852 272 Z"/>
    <path d="M866 234 Q860 244 866 248 Q872 244 866 234 Z" fill="#3f6e38"/>
    <circle cx="925" cy="276" r="26" fill="none" stroke="var(--icon)" stroke-width="7"/>
    <circle cx="925" cy="276" r="7"/>
    <path d="M925 276 L925 252 M925 276 L948 268 M925 276 L940 297 M925 276 L910 297 M925 276 L902 268" stroke="var(--icon)" stroke-width="7"/>
  </g>

  <!-- company icon: buildings -->
  <g class="icon-company" fill="var(--icon)">
    <rect x="249" y="588" width="18" height="70"/>
    <rect x="272" y="572" width="26" height="86"/>
    <rect x="301" y="580" width="14" height="78"/>
    <rect x="318" y="605" width="12" height="53"/>
    <rect x="331" y="612" width="6" height="46"/>
    <g fill="#3f6e38">
      <rect x="278" y="580" width="3" height="3"/><rect x="286" y="580" width="3" height="3"/>
      <rect x="278" y="590" width="3" height="3"/><rect x="286" y="590" width="3" height="3"/>
      <rect x="278" y="600" width="3" height="3"/><rect x="286" y="600" width="3" height="3"/>
      <rect x="278" y="610" width="3" height="3"/><rect x="286" y="610" width="3" height="3"/>
      <rect x="278" y="620" width="3" height="3"/><rect x="286" y="620" width="3" height="3"/>
      <rect x="255" y="642" width="6" height="16"/>
    </g>
  </g>

  <!-- cost to manage icon: dollar with arrows -->
  <g class="icon-manage" stroke="var(--icon)" stroke-width="4" fill="none">
    <circle cx="880" cy="642" r="24"/>
    <path d="M880 612 L880 572 M898 624 L935 590 M910 642 L952 642"/>
    <g fill="var(--icon)" stroke="none">
      <polygon points="873,574 880,560 887,574"/>
      <polygon points="929,586 944,582 939,596"/>
      <polygon points="948,635 963,642 948,649"/>
    </g>
    <text x="880" y="653" text-anchor="middle" font-family="Source Sans 3, sans-serif" font-weight="700" font-size="30" fill="var(--icon)" stroke="none">$</text>
  </g>

  <!-- hub tile -->
  <rect class="hub-tile" x="482" y="320" width="212" height="213" rx="44" fill="url(#tile-blue)" stroke="var(--blue-rim)" stroke-width="4"/>
  <g class="hub-cars">
    <use href="#car" x="519" y="351" width="56" height="26"/>
    <use href="#car" x="588" y="351" width="56" height="26"/>
    <use href="#car" x="524" y="397" width="56" height="26"/>
    <use href="#car" x="594" y="397" width="56" height="26"/>
    <use href="#car" x="524" y="444" width="56" height="26"/>
    <use href="#car" x="594" y="444" width="56" height="26"/>
    <ellipse cx="622" cy="410" rx="38" ry="25" fill="none" stroke="var(--icon)" stroke-width="2" transform="rotate(-8 622 410)"/>
  </g>
</svg>

<div class="stage-label label-end-of-life">
  <h2 class="stage-title">End of Life</h2>
  <ul class="stage-items"><li>Disposal Costs</li></ul>
</div>
<div class="stage-label label-cost-to-run">
  <h2 class="stage-title">Cost to Run</h2>
  <ul class="stage-items"><li>Lease</li><li>Finance &amp; Tax</li><li>Insurance</li></ul>
</div>
<div class="stage-label label-company">
  <h2 class="stage-title">Your Company</h2>
  <ul class="stage-items"><li>Safety</li><li>Sustainability</li><li>Specifications</li></ul>
</div>
<div class="stage-label label-cost-to-manage">
  <h2 class="stage-title">Cost to<br>Manage</h2>
  <ul class="stage-items"><li>Lease</li><li>Finance &amp; Tax</li><li>Insurance</li></ul>
</div>
<div class="hub-caption">Best fit for purpose</div>
</body>
</html>
```